Breezeway Travel NI needs a new Website

We have an old website that is just that - old. We need a fresh website that is professional graphic designed that has the following features.
1. Can be updated by ourselves in some areas.
2. Has a shopping cart.
3. Has links to download PDF files
4. Has links to other pages in the website
5. Includes social media links
6. Has a client log-in area
Full details in brief provided.

SORRY BUT IT'S URGENT. We've taken too long to write the details and it is now urgent. So my apologies I will be asking for designers to work quickly.

We will continue to use our existing web hosting company and url. Their is a link to the old website in the Design Brief.
Updates

UPDATE:  Please see the new file UPDATE TO DESIGN BRIEF.
Thanks for all your submissions to date.  We hope the update will assist with your designs.
As indicated in previous messages, we are happy with the Home Page + 1 Page in order to select the designer to work with in creating the full design. 

Thankyou Designers.  Much appreciate your efforts.
It's getting late here on Norfolk so I won't have much chance too review any more designs this evening.
But for your information:
Designer 3817405 Ravindra Sethi is so far the closest to what we are seeking.
Thanks again. 

Reason: Have extended to Monday 7 October to give time for designers to submit after feedback today. Especially given the time differences

Target Market(s)

Very wide audience. Current client group not that tech savvy, but we hope to broaden our market and sell more creative products, and so website needs to consider how people now use media, ie tablets & iphones.

Industry/Entity Type

Shopping

Requirements
Nice to have
• PLEASE SEE THE "UPDATE TO THE DESIGN BRIEF"

```html
<!DOCTYPE html>
<html lang="en">
<head>
<meta charset="utf-8">
<title>Breezeway Travel – Home</title>
<link rel="stylesheet" href="https://fonts.googleapis.com/css2?family=Fjalla+One&family=Michroma&family=Arimo:wght@400;700&display=swap">
<style>
:root{
  --bg:#3b3b3b;
  --orange:#f28a22;
  --text:#d6d6d6;
  --muted:#a9a9a9;
  --rule:#6a6a6a;
  --white:#f2f2f2;
  --frame:#e8913a;
}
*{margin:0;padding:0;box-sizing:border-box}
html,body{width:1200px;height:733px;overflow:hidden;background:var(--bg)}
body{position:relative;font-family:"Arimo",Arial,sans-serif;color:var(--text)}
.abs{position:absolute}
.brand{left:150px;top:40px;width:220px}
.brand-name{font-family:"Fjalla One",sans-serif;font-size:27px;line-height:28px;color:var(--white);text-transform:uppercase;letter-spacing:.5px}
.info-label{font-family:"Michroma",sans-serif;font-size:11px;font-weight:700;color:var(--orange);letter-spacing:.5px;margin-bottom:1px}
.info{font-size:11.3px;line-height:13.6px;color:var(--text)}
.info p{white-space:pre}
.location{left:697px;top:22px}
.contact{left:862px;top:22px}
.hrule{height:1px;background:var(--rule)}
.vrule{width:1px;background:var(--rule)}
.nav{left:150px;top:130px;width:172px;list-style:none}
.nav li{height:29.2px;border-bottom:1px dashed #5f5f5f;font-family:"Fjalla One",sans-serif;font-size:14.5px;line-height:29px;padding-left:8px;color:#b9b9b9;text-transform:uppercase}
.nav li.current{color:var(--orange)}
.headline{left:331px;width:523px;text-align:center;font-family:"Fjalla One",sans-serif;text-transform:uppercase}
.title{top:146px;font-size:27px;color:var(--orange);line-height:32px}
.subtitle{top:177px;font-size:18px;color:#dcdcdc;line-height:22px}
.promotes{left:354px;top:220px;width:476px;display:flex;align-items:center;gap:14px}
.promotes span.line{flex:1;height:1px;background:var(--rule)}
.promotes span.word{font-family:"Michroma",sans-serif;font-weight:700;font-size:12px;color:var(--orange);letter-spacing:1px}
.values{left:354px;top:242px;width:476px;display:flex;justify-content:center;align-items:center;gap:14px;font-family:"Fjalla One",sans-serif;font-size:17px;color:#c2c2c2}
.sq{display:inline-block;width:4px;height:4px;border:1px solid #9a9a9a}
.photo{border:12px solid var(--frame);border-bottom-width:24px;box-shadow:3px 5px 10px rgba(0,0,0,.45)}
.photo-a{left:352px;top:310px;width:266px;height:198px;transform:rotate(-1deg);background:linear-gradient(180deg,#bdbdbd,#777 60%,#4e4e4e)}
.photo-b{left:582px;top:290px;width:236px;height:230px;transform:rotate(5deg);background:linear-gradient(180deg,#d2d2d2,#6f6f6f 55%,#3e3e3e)}
.supported-label{left:354px;top:542px;font-family:"Fjalla One",sans-serif;font-size:14px;color:var(--orange)}
.supported{left:356px;top:566px;list-style:none;font-size:12px;line-height:20.3px;color:#ececec}
.supported li{display:flex;align-items:center;gap:8px}
.divider{left:466px;top:541px}
.audience-title{left:493px;top:541px;font-family:"Fjalla One",sans-serif;text-transform:uppercase;line-height:22px}
.audience-title .l1{font-size:22px;color:var(--white)}
.audience-title .l2{font-size:16.5px;color:#c9c9c9;line-height:18px}
.audience{left:493px;top:601px;font-size:13px;line-height:22px;color:#bcbcbc}
.audience p{display:flex;align-items:center;gap:8px}
.side-title{left:854px;width:196px;top:140px;text-align:center;font-family:"Fjalla One",sans-serif;font-size:19px;color:var(--orange)}
.video{left:868px;top:170px;width:168px;height:102px;background:linear-gradient(180deg,#111 0,#4a3e1c 45%,#111 90%);border-bottom:8px solid #222}
.video-note{left:868px;top:281px;font-size:10px;color:#bcbcbc}
.social-row{left:868px;top:293px;display:flex;align-items:center;gap:6px;font-size:13px;color:#c9c9c9}
.social-row b{color:var(--white);font-weight:700}
.like{display:inline-block;width:40px;height:15px;border:1px solid #bbb;border-radius:2px;background:#e6e6e6;color:#333;font-size:9px;line-height:13px;text-align:center}
.login{left:866px;top:337px;width:167px;height:27px;border-radius:3px;background:linear-gradient(180deg,#fafafa,#cfcfcf);font-family:"Michroma",sans-serif;font-weight:700;font-size:14px;color:#555;text-align:center;line-height:27px}
.promo{left:866px;width:167px;overflow:hidden}
.festival{top:378px;height:117px;background:linear-gradient(180deg,#1c3f7a,#3b6fb0 40%,#1a2f55)}
.festival .name{position:absolute;left:8px;top:10px;font-weight:700;font-size:19px;line-height:17px;color:#fff}
.festival .band{position:absolute;left:0;top:52px;width:100%;height:38px;background:rgba(20,20,20,.75);padding:5px 10px;font-size:10px;font-weight:700;line-height:12px;color:#fff}
.festival .cta{position:absolute;left:10px;top:93px;font-size:10px;font-weight:700;color:var(--orange)}
.support{top:510px;height:136px;background:linear-gradient(160deg,#7c9e6a,#3e6a34 55%,#6b6254)}
.support .band{position:absolute;left:0;top:78px;width:100%;height:36px;background:rgba(30,30,30,.7);font-family:"Fjalla One",sans-serif;font-size:24px;line-height:36px;color:var(--orange);padding-left:24px}
.copyright{left:0;width:1200px;top:707px;text-align:center;font-size:10px;color:#dcdcdc}
</style>
</head>
<body>
<div class="abs brand"><div class="brand-name">Breezeway<br>Travel</div></div>

<div class="abs location">
  <div class="info-label">LOCATION</div>
  <div class="info"><p>Ferncliff Road, Pinehaven</p><p>PO Box 514</p><p>Kestrel Island NSW 2914</p><p>SOUTH PACIFIC</p><p>N.B.N. 415 826 307</p></div>
</div>
<div class="abs contact">
  <div class="info-label">CONTACT</div>
  <div class="info"><p>International:  + 67 23 51873</p><p>Australia:        1800 614 382</p><p>New Zealand:  0000 000 000</p><p> </p><p>Email: hello@breezewaytravel.org</p><p>Linkbook: breezewaytravel</p></div>
</div>

<div class="abs hrule" style="left:150px;top:128px;width:900px"></div>
<div class="abs vrule" style="left:331px;top:128px;height:568px"></div>
<div class="abs vrule" style="left:854px;top:128px;height:568px"></div>
<div class="abs hrule" style="left:150px;top:696px;width:900px"></div>

<ul class="abs nav">
  <li class="current">Home</li><li>Governance</li><li>Our Mission &amp; Values</li><li>Our Facilitators</li><li>Kestrel Island</li><li>Services</li><li>Holiday Programs</li><li>Design Your Own Holiday</li><li>Kite Creative Projects</li><li>Schoolies Siblings Family</li><li>Our Shop</li><li>Make a Booking</li><li>Testimonials</li>
</ul>

<div class="abs headline title">Our Social Enterprise</div>
<div class="abs headline subtitle">Established March 2004</div>
<div class="abs promotes"><span class="line"></span><span class="word">PROMOTES</span><span class="line"></span></div>
<div class="abs values"><span>DIVERSITY</span><span class="sq"></span><span>CARING</span><span class="sq"></span><span>COMMUNITY</span><span class="sq"></span><span>KESTREL ISLAND</span></div>
<div class="abs hrule" style="left:354px;top:276px;width:476px"></div>

<div class="abs photo photo-b" role="img" aria-label="Black and white photo of a group of travellers standing by old stone ruins"></div>
<div class="abs photo photo-a" role="img" aria-label="Black and white photo of travellers riding camels along a beach"></div>

<div class="abs supported-label">SUPPORTED</div>
<ul class="abs supported">
  <li><span class="sq"></span>Holidays</li><li><span class="sq"></span>Travel</li><li><span class="sq"></span>Recreation</li><li><span class="sq"></span>Respite</li><li><span class="sq"></span>Creative projects</li>
</ul>
<svg class="abs divider" width="12" height="126" viewBox="0 0 12 126"><path d="M1 0V56L7 62L1 68V126" fill="none" stroke="#8a8a8a" stroke-width="1"/></svg>

<div class="abs audience-title"><div class="l1">For people requiring support to</div><div class="l2">Participate in socially inclusive events.</div></div>
<div class="abs audience">
  <p>Intellectual Disability <span class="sq"></span> Acquired Brain Injury <span class="sq"></span></p>
  <p>Mental Health <span class="sq"></span> Sensory Impairment <span class="sq"></span> Frail Aged <span class="sq"></span></p>
  <p>Mobility Challenged <span class="sq"></span> Siblings of children with Disabilities</p>
</div>

<div class="abs side-title">IMAGES &amp; VIDEO</div>
<div class="abs video" role="img" aria-label="Video player showing a film strip still"></div>
<div class="abs video-note">to see more photographs and video's</div>
<div class="abs social-row"><span class="like">Like</span><span>our <b>LINKBOOK</b> page</span></div>
<div class="abs login">CLIENT LOGIN</div>

<div class="abs promo festival" role="img" aria-label="Kite Film Festival banner with a film strip over a coastal scene">
  <div class="name">KITE FILM<br>FESTIVAL</div>
  <div class="band">LOREM IPSUM DOLOR SIT<br>AMET CONSECTETUR</div>
  <div class="cta">CLICK TO LEARN MORE</div>
</div>
<div class="abs promo support" role="img" aria-label="Photo of a smiling traveller outdoors among trees">
  <div class="band">SUPPORT US</div>
</div>

<div class="abs copyright">© Copyright Breezeway Travel 2013. All Rights Reserved.</div>
</body>
</html>
```